Simple and Clean business card design

We would like the design to be simple clean and to incorporate our colors.

We are open to your design and talent, we have the dots in our logo as we think of it as data points and we connect data points for people.

We are open to see the great creative and clean design you bring to the table

Contact Information for Business Card

please include: name, position, email, phone and website

Font styles to use
Sans Serif

Requirements
Must have
• my colors incorporated, simplicity
Nice to have
• lots of white space, simplicity
Should not have
• complexicity/ complex art

```html
<!DOCTYPE html>
<html lang="en">
<head>
<meta charset="utf-8">
<title>Nectra Business Card</title>
<link rel="stylesheet" href="https://fonts.googleapis.com/css2?family=Montserrat:wght@500;600;700&display=swap">
<style>
  :root {
    --stage: #262626;
    --card: #0c0c0c;
    --ink: #ffffff;
    --accent-blue: #4285f4;
    --divider: #3a3a3a;
  }
  * { box-sizing: border-box; margin: 0; padding: 0; }
  html, body {
    width: 1200px;
    height: 900px;
    overflow: hidden;
    background: var(--stage);
    font-family: "Montserrat", Arial, sans-serif;
  }
  .stage {
    width: 1200px;
    height: 900px;
    display: flex;
    align-items: center;
    justify-content: center;
    gap: 50px;
  }
  .card {
    width: 525px;
    height: 300px;
    background: var(--card);
    border-radius: 22px;
    position: relative;
    overflow: hidden;
  }
  .wordmark {
    display: flex;
    align-items: center;
    gap: 10px;
    color: var(--ink);
    font-weight: 700;
    letter-spacing: 0.5px;
  }
  .wordmark-dot {
    width: 14px;
    height: 14px;
    border-radius: 50%;
    background: var(--accent-blue);
  }
  .card-contact .wordmark {
    position: absolute;
    left: 40px;
    top: 128px;
    font-size: 44px;
  }
  .card-divider {
    position: absolute;
    left: 262px;
    top: 40px;
    width: 1px;
    height: 220px;
    background: var(--divider);
  }
  .contact-block {
    position: absolute;
    left: 288px;
    top: 78px;
  }
  .person-name {
    color: var(--accent-blue);
    font-size: 22px;
    font-weight: 700;
    line-height: 1.1;
  }
  .person-role {
    color: var(--ink);
    font-size: 13px;
    font-weight: 500;
    margin-top: 3px;
  }
  .contact-list {
    list-style: none;
    margin-top: 26px;
  }
  .contact-item {
    display: flex;
    align-items: center;
    gap: 8px;
    color: var(--ink);
    font-size: 12.5px;
    font-weight: 500;
    margin-bottom: 7px;
  }
  .contact-icon {
    width: 18px;
    height: 18px;
    flex: none;
  }
  .card-front {
    display: flex;
    align-items: center;
    justify-content: center;
  }
  .card-front .wordmark {
    font-size: 52px;
  }
  .card-front .wordmark-dot {
    width: 16px;
    height: 16px;
  }
</style>
</head>
<body>
<main class="stage">
  <section class="card card-contact">
    <div class="wordmark"><span class="wordmark-dot"></span>nectra</div>
    <div class="card-divider"></div>
    <div class="contact-block">
      <p class="person-name">Daniel Reyes</p>
      <p class="person-role">Founder/ CEO</p>
      <ul class="contact-list">
        <li class="contact-item">
          <svg class="contact-icon" viewBox="0 0 18 18" fill="none" stroke="var(--accent-blue)" stroke-width="1.4">
            <circle cx="9" cy="9" r="8"/>
            <path d="M6.2 5.2l1.3 1.6-.8 1c.5 1 1.3 1.8 2.3 2.3l1-.8 1.6 1.3-.7 1.2c-2.6-.4-4.8-2.6-5.2-5.2z" stroke-linejoin="round"/>
          </svg>
          555-214-0187
        </li>
        <li class="contact-item">
          <svg class="contact-icon" viewBox="0 0 18 18" fill="none" stroke="var(--accent-blue)" stroke-width="1.4">
            <circle cx="9" cy="9" r="8"/>
            <rect x="5" y="6" width="8" height="6" rx="0.8"/>
            <path d="M5 6.3l4 3 4-3"/>
          </svg>
          daniel.reyes@nectra.one
        </li>
        <li class="contact-item">
          <svg class="contact-icon" viewBox="0 0 18 18" fill="none" stroke="var(--accent-blue)" stroke-width="1.4">
            <circle cx="9" cy="9" r="8"/>
            <circle cx="9" cy="9" r="4.5"/>
            <path d="M4.5 9h9M9 4.5c-1.6 1.3-1.6 7.7 0 9M9 4.5c1.6 1.3 1.6 7.7 0 9"/>
          </svg>
          www.nectra.one
        </li>
      </ul>
    </div>
  </section>
  <section class="card card-front">
    <div class="wordmark"><span class="wordmark-dot"></span>nectra</div>
  </section>
</main>
</body>
</html>
```